Vending machine company website for SnackHarbor

We need a website for our vending machine services company. It will be based on another website that a friend has. My URL is snackharbor.com and the one I'm trying to emulate with my own logo and colors is pantrybloxo.com.

This will be roughly 6 total pages with one being an opt-in/opt-out page for SMS messages, one being a contact form, etc.

I want to use the logo I purchased from this site that I have attached.

The goal is to be clean, professional, intuitive and easy navigation, etc.

The only difference between my site and the reference site should be that we are not offering coffee service.

I will need all of the code for the site, and it should not use any CMS things like Joomla, Wordpress, etc.

Our actual machines are this model minus the green highlights.f

https://www.kelvomat.com/krx-pdl-mq-snack-and-drink-vending-machine-374.html

Target Market(s)

Companies that want to have vending machine services, or to buy or lease vending machines

Industry/Entity Type

Vending machines for snacks and drinks either placed at locations like apartment complexes, waiting rooms for tire centers, office building break rooms, etc. also vending machine repair services, or selling or leasing vending machines to those interested in getting into the business.

Coding

Coded - Design and coding required

Number of Pages Required

5+ page

Font styles to use
Sans Serif

Requirements
Must have
• It will be similar to pantrybloxo.com in terms of pages, categories, etc. but with our logo, colors, etc. and should be clean and professional. It will have the same pages plus one other page for opt-in or opt-out of SMS messages
Nice to have
• Clean graphics and perhaps some AI designs for vending machine repair, just like the one they use on the pantrybloxo.com site. We would like multiple photos on the home page cycling where you see very attractive people shopping for snacks and drinks at the machines with the items blurred, or people sitting around laughing and smiling while enjoying snacks or drinks at a campus break room, or picnic table, or outside with the machine behind them. Please search for KRX-PDL-47M(B2) Snack And Drink Vending Machine at kelvomat
Should not have
• It can not be designed for CRM like WordPress, Joomla, etc. and should be clean new code, that doesn't attract hackers and it shouldn't be too busy.

```html
<!DOCTYPE html>
<html lang="en">
<head>
<meta charset="utf-8">
<title>SnackHarbor — Vending Services</title>
<link href="https://fonts.googleapis.com/css2?family=Poppins:wght@300;400;500;600;700&family=Lora:ital@1&display=swap" rel="stylesheet">
<style>
:root{
  --orange:#e6962e;
  --navy:#0e1526;
  --slate:#4a4a4d;
  --ink:#222;
  --charcoal:#2a2a2b;
  --mist:#efefef;
  --muted:#777;
  --white:#fff;
}
*{box-sizing:border-box;margin:0;padding:0}
html,body{width:1200px;height:4926px;overflow:hidden}
body{font-family:"Poppins",sans-serif;color:var(--ink);background:var(--white)}
.btn{display:inline-block;border-radius:20px;font-size:11px;font-weight:600;padding:9px 30px;background:var(--orange);color:var(--white)}
.btn-dark{background:var(--ink);color:var(--white)}
.btn-grey{background:#555;color:var(--white)}
.eyebrow{color:var(--orange);font-size:11px;font-weight:500;text-align:center}
.section-title{font-size:28px;font-weight:600;text-align:center;margin-top:6px}
.brand{font-weight:500;color:var(--orange);font-size:40px;letter-spacing:-.5px;display:flex;align-items:center;gap:8px}
.brand .dot{width:14px;height:14px;border-radius:50%;background:var(--orange)}
.ph{position:absolute}

/* header */
.site-header{height:91px;position:relative;box-shadow:0 2px 6px rgba(0,0,0,.05)}
.site-header .brand{position:absolute;left:105px;top:18px}
.topbar{position:absolute;right:105px;top:6px;display:flex;align-items:center;gap:14px;font-size:10px}
.topbar .btn{padding:7px 22px;font-size:10px}
.topbar svg{vertical-align:middle;margin-right:4px}
.main-nav{position:absolute;right:105px;top:56px;display:flex;gap:34px;font-size:11px;font-weight:500}
.main-nav .active{color:var(--orange);border-bottom:2px solid var(--orange)}

/* hero */
.hero{height:992px;position:relative;overflow:hidden;color:var(--white)}
.hero-bg{position:absolute;inset:0}
.hero-copy{position:absolute;left:105px;top:150px}
.hero-copy h1{font-size:35px;font-weight:600}
.hero-copy p{font-size:13px;font-weight:500;margin:12px 0 26px;width:500px}
.machine-photo{left:689px;top:44px;width:284px;height:596px;border-radius:8px;background:linear-gradient(180deg,#c98a3a,#5b3a1a 8%,#1c1c22 30%,#2a1b18 80%,#9a6a30)}
.city-photo{left:131px;top:462px;width:380px;height:380px;border-radius:50%;background:radial-gradient(circle at 40% 30%,#6aa6e0,#3b6ea8 45%,#8e949c 75%,#5c6166)}
.welcome{position:absolute;left:612px;top:685px;width:400px}
.welcome .eyebrow{text-align:left}
.welcome h2{font-size:26px;font-weight:600;margin:4px 0 18px}
.welcome p{font-size:10.5px;line-height:1.75;margin-bottom:22px}

/* machines */
.machines{height:591px;padding-top:70px}
.machine-cards{display:flex;justify-content:center;gap:20px;margin-top:30px}
.machine-card{width:318px;position:relative;height:400px}
.machine-card .frame{position:absolute;left:0;right:0;top:248px;height:150px;border:1px solid #d6d6d6;border-top:none}
.machine-card .frame::before,.machine-card .frame::after{content:"";position:absolute;top:0;height:1px;width:80px;background:#d6d6d6}
.machine-card .frame::before{left:0}.machine-card .frame::after{right:0}
.machine-card .halo{position:absolute;left:70px;top:40px;width:178px;height:178px;border-radius:50%;background:#f1f1f1}
.machine-card .unit{position:absolute;left:119px;top:0;width:80px;height:210px;border-radius:3px}
.unit-compact{background:linear-gradient(90deg,#d8dde5,#f5f7fa 40%,#c7ccd4)}
.unit-standard{background:linear-gradient(90deg,#cfd4da,#f3f4f6 45%,#d23a2e 80%,#b52b22)}
.machine-card h3{position:absolute;top:270px;width:100%;text-align:center;font-size:14px;font-weight:500}
.machine-card p{position:absolute;top:295px;left:30px;right:30px;text-align:center;font-size:8.5px;color:var(--muted)}
.machine-card .btn{position:absolute;top:382px;left:50%;transform:translateX(-50%);padding:8px 28px;font-size:9px}

/* features */
.features{height:593px;background:var(--orange);position:relative}
.features .eyebrow{color:var(--ink);padding-top:70px}
.features .section-title{color:var(--ink);font-size:24px}
.core{position:absolute;left:490px;top:202px;width:220px;height:220px;border-radius:50%;background:var(--white);border:9px solid var(--ink);display:flex;align-items:center;justify-content:center}
.core .brand{font-size:24px}
.ring{position:absolute;left:455px;top:167px;width:290px;height:290px;border-radius:50%;border:1.5px solid var(--white)}
.feat{position:absolute;width:300px;color:var(--white)}
.feat h4{font-size:15px;font-weight:400;margin-bottom:10px}
.feat p{font-size:9px;line-height:1.6}
.feat.l{text-align:right;left:105px}
.feat.r{left:794px}
.ficon{position:absolute;width:50px;height:50px;border-radius:50%;border:3px solid var(--ink);background:var(--orange);display:flex;align-items:center;justify-content:center}
.features .btn{position:absolute;left:50%;transform:translateX(-50%);top:494px}

/* monitoring */
.monitor{height:497px;position:relative}
.monitor h2{position:absolute;left:105px;top:98px;font-size:37px;font-weight:600;line-height:1.25}
.monitor h2 span{color:var(--orange)}
.monitor .lead{position:absolute;left:105px;top:225px;font-size:21px;font-weight:300;line-height:1.4;width:460px}
.monitor .btn{position:absolute;left:105px;top:355px}
.tracker{left:803px;top:208px;width:113px;height:233px;background:linear-gradient(90deg,#c9ccd1,#f1f2f3 50%,#b6b9bf);border-radius:3px}
.slot{position:absolute;width:96px;height:98px;border:1.5px solid var(--orange);background:var(--white);border-radius:3px}
.slot .item{position:absolute;left:24px;top:14px;width:46px;height:46px;border-radius:4px}
.slot .meta{position:absolute;left:0;right:0;bottom:0;height:20px;background:#555;color:var(--white);font-size:8px;display:flex;justify-content:space-between;padding:4px 6px}
.slot .no{position:absolute;left:-9px;top:-9px;width:18px;height:18px;border-radius:50%;background:var(--orange);color:var(--white);font-size:9px;text-align:center;line-height:18px}

/* testimonials */
.reviews{height:448px;background:var(--charcoal);color:var(--white);position:relative}
.reviews .eyebrow{padding-top:70px}
.reviews .section-title{font-size:24px}
.quote-box{position:absolute;left:295px;top:155px;width:610px;height:165px;border:1px solid var(--orange);text-align:center;padding:26px 60px}
.quote-box .stars{color:var(--orange);font-size:14px;letter-spacing:2px}
.quote-box p{font-family:"Lora",serif;font-style:italic;font-size:10.5px;line-height:1.7;margin:8px 0 14px}
.quote-box .name{color:var(--orange);font-size:9px;font-weight:600;letter-spacing:.5px}
.qmark{position:absolute;color:var(--orange);font-size:44px;font-family:"Lora",serif;line-height:1;font-weight:700}
.arrow{position:absolute;top:230px;font-size:16px;color:#ccc}
.reviews .btn{position:absolute;left:50%;transform:translateX(-50%);top:355px}

/* partners */
.partners{height:328px;background:var(--mist);position:relative}
.partners .section-title{padding-top:70px;font-size:24px}
.partner-row{position:absolute;left:232px;top:135px;display:flex;gap:12px}
.partner-badge{width:117px;height:66px;background:var(--white);display:flex;align-items:center;justify-content:center}
.partner-badge span{width:70px;height:30px;border-radius:15px;background:#c9cdd3}
.pager{position:absolute;left:50%;transform:translateX(-50%);top:238px;display:flex;gap:6px}
.pager span{width:28px;height:28px;border-radius:50%;border:1.5px solid #aaa;font-size:12px;color:#888;text-align:center;line-height:24px}

/* faq */
.faq{height:497px;position:relative}
.faq .section-title{padding-top:72px;font-size:25px}
.faq-list{position:absolute;left:255px;top:148px;width:690px}
.faq-item{display:flex;gap:30px;font-size:10.5px;font-weight:500;padding:14px 26px;border-bottom:1px solid #eee}
.faq-item .plus{color:var(--orange);font-size:15px;line-height:12px}
.faq-item.open{box-shadow:0 3px 12px rgba(0,0,0,.12);padding:16px 26px 18px}
.faq-item.open small{display:block;font-weight:400;font-size:9px;color:var(--muted);margin-top:8px}
.faq .btn{position:absolute;left:50%;transform:translateX(-50%);top:428px}

/* cta */
.cta{height:579px;position:relative;color:var(--white);overflow:hidden}
.cta-bg{position:absolute;inset:0}
.cta h2{position:absolute;top:250px;width:100%;text-align:center;color:var(--orange);font-size:26px;font-weight:600}
.cta .intro{position:absolute;top:296px;left:340px;width:520px;text-align:center;font-size:11px;line-height:1.5}
.lead-form{position:absolute;left:340px;top:368px;width:520px;display:grid;grid-template-columns:1fr 1fr;gap:12px 16px}
.lead-form .field{height:30px;border:1px solid #aaa;border-radius:16px;font-size:9px;padding:8px 16px;background:rgba(255,255,255,.05)}
.lead-form .wide{grid-column:1/3}
.cta .btn{position:absolute;left:50%;transform:translateX(-50%);top:506px;padding:10px 40px}

/* footer */
.site-footer{height:310px;position:relative;font-size:10px}
.site-footer .brand{position:absolute;left:200px;top:60px;font-size:32px}
.fcol{position:absolute;top:68px}
.fcol h5{font-size:11px;font-weight:600;margin-bottom:14px}
.fcol li{list-style:none;margin-bottom:8px;display:flex;gap:8px}
.links{display:grid;grid-template-columns:90px 90px;font-size:9px;row-gap:8px}
.social{position:absolute;left:972px;top:68px;display:flex;flex-direction:column;gap:8px}
.social span{width:26px;height:26px;border-radius:50%;background:var(--ink)}
.social span.on{background:var(--orange)}
.copy{position:absolute;left:200px;top:255px;font-size:8.5px}
.copy b{color:var(--orange);font-weight:400}
.to-top{position:absolute;left:1052px;top:248px}
</style>
</head>
<body>

<header class="site-header">
  <div class="brand"><span class="dot"></span>SnackHarbor</div>
  <div class="topbar">
    <span><svg width="11" height="11" viewBox="0 0 24 24"><path d="M6 2l4 5-2 3a12 12 0 006 6l3-2 5 4-3 4C10 22 2 14 2 5z" fill="#e6962e"/></svg>555-014-2298</span>
    <span>/</span>
    <span><svg width="11" height="11" viewBox="0 0 24 24"><rect x="2" y="5" width="20" height="14" rx="2" fill="#e6962e"/></svg>info@snackharbor.com</span>
    <span class="btn">Inquire Now!</span>
  </div>
  <nav class="main-nav">
    <span class="active">Home</span><span>About Us</span><span>Our Machines</span><span>Services</span><span>Products</span><span>FAQ</span><span>Contact Us</span>
  </nav>
</header>

<section class="hero">
  <svg class="hero-bg" width="1200" height="992" viewBox="0 0 1200 992" preserveAspectRatio="none">
    <rect width="1200" height="992" fill="#0e1526"/>
    <path d="M0,520 C180,380 360,380 540,520 C700,650 900,700 1200,560 L1200,992 L0,992 Z" fill="#e6962e"/>
    <path d="M0,560 C180,430 360,430 540,560 C700,680 900,720 1200,610 L1200,992 L0,992 Z" fill="#4a4a4d"/>
  </svg>
  <div class="ph machine-photo" role="img" aria-label="Illuminated snack and drink vending machine stocked with products"></div>
  <div class="hero-copy">
    <h1>Elevate Your Workplace</h1>
    <p>Leader in Trailblazing Contactless, Self-Service Vending Machines from San Francisco to Monterey</p>
    <span class="btn">Inquire Now!</span>
  </div>
  <div class="ph city-photo" role="img" aria-label="City skyline with modern tower seen through a circular frame"></div>
  <div class="welcome">
    <div class="eyebrow">Welcome to</div>
    <h2>SnackHarbor</h2>
    <p>SnackHarbor is a locally owned and professionally operated, full service vending business that provides vending machine placement and exceptional services to privately owned businesses, large corporations, and government agencies at no cost. With multiple warehouses, our team is able to cover a wide area of the greater San Francisco Bay Area and Santa Cruz Central Coast.</p>
    <span class="btn">Explore More</span>
  </div>
</section>

<section class="machines">
  <div class="eyebrow">Our Machines</div>
  <h2 class="section-title" style="font-size:25px">Combo SnackHarbor Machines</h2>
  <div class="machine-cards">
    <div class="machine-card">
      <div class="halo"></div>
      <div class="unit unit-compact" role="img" aria-label="Compact combo vending machine"></div>
      <div class="frame"></div>
      <h3>Compact Combo</h3>
      <p>Specifically tailored for locations with limited space or businesses that have fewer staff and customers.</p>
      <span class="btn">Learn More</span>
    </div>
    <div class="machine-card">
      <div class="halo"></div>
      <div class="unit unit-standard" role="img" aria-label="Standard combo vending machine"></div>
      <div class="frame"></div>
      <h3>Standard Combo</h3>
      <p>Vending machines that combine snacks and drinks cater to a diverse range of customers.</p>
      <span class="btn btn-dark">Learn More</span>
    </div>
  </div>
</section>

<section class="features">
  <div class="eyebrow">SnackHarbor</div>
  <h2 class="section-title">Features &amp; Benefits</h2>
  <div class="ring"></div>
  <div class="core"><div class="brand">SnackHarbor</div></div>
  <div class="feat l" style="top:158px"><h4>Remote Inventory Monitoring</h4><p>Our real-time remote inventory management delivers superior service based on the needs of each location.</p></div>
  <div class="feat l" style="top:348px"><h4>Contactless Payment</h4><p>Our machines use the latest card readers to accept CardLink, PayNova, Amerix Card, TapWallet and QuickTap.</p></div>
  <div class="feat r" style="top:158px"><h4>Hands off Participation</h4><p>We provide all energy efficient vending machines, maintenance and repairs free of charge to our clients.</p></div>
  <div class="feat r" style="top:348px"><h4>Customizable</h4><p>If there is a product that is requested or needs to be removed for dietary restrictions, safety, or preference, our team will work with you on the request.</p></div>
  <div class="ficon" style="left:440px;top:200px"><svg width="20" height="20" viewBox="0 0 24 24"><rect x="5" y="3" width="14" height="18" rx="2" fill="none" stroke="#fff" stroke-width="2"/></svg></div>
  <div class="ficon" style="left:440px;top:380px"><svg width="20" height="20" viewBox="0 0 24 24"><rect x="3" y="6" width="18" height="12" rx="2" fill="none" stroke="#fff" stroke-width="2"/></svg></div>
  <div class="ficon" style="left:710px;top:200px"><svg width="20" height="20" viewBox="0 0 24 24"><path d="M5 13l4 4 10-10" fill="none" stroke="#fff" stroke-width="2"/></svg></div>
  <div class="ficon" style="left:710px;top:380px"><svg width="20" height="20" viewBox="0 0 24 24"><circle cx="12" cy="12" r="7" fill="none" stroke="#fff" stroke-width="2"/></svg></div>
  <span class="btn btn-dark">Inquire Now!</span>
</section>

<section class="monitor">
  <h2><span>24 Hour</span> live<br>inventory monitoring</h2>
  <p class="lead">We track it, so you don't have to! Consistent service and superior experience.</p>
  <span class="btn">Inquire Now!</span>
  <svg class="ph" style="left:0;top:0" width="1200" height="497" viewBox="0 0 1200 497">
    <g stroke="#e6962e" stroke-width="1.2" fill="none">
      <path d="M823 171 L840 230"/><path d="M950 160 L890 240"/><path d="M762 200 L820 260"/><path d="M997 200 L905 280"/><path d="M713 310 L810 330"/><path d="M997 310 L910 340"/>
    </g>
  </svg>
  <div class="ph tracker" role="img" aria-label="Vending machine with live stock view"></div>
  <div class="slot" style="left:777px;top:73px"><span class="no">5</span><div class="item" style="background:#c73a2e"></div><div class="meta"><span>6/12</span><span>$1.75</span></div></div>
  <div class="slot" style="left:921px;top:85px"><span class="no">6</span><div class="item" style="background:#d8a6b8"></div><div class="meta"><span>11/12</span><span>$1.50</span></div></div>
  <div class="slot" style="left:662px;top:145px"><span class="no">2</span><div class="item" style="background:#e9c64a"></div><div class="meta"><span>3/9</span><span>$4.00</span></div></div>
  <div class="slot" style="left:997px;top:145px"><span class="no">3</span><div class="item" style="background:#3a7abf"></div><div class="meta"><span>5/9</span><span>$3.00</span></div></div>
  <div class="slot" style="left:614px;top:258px"><span class="no">1</span><div class="item" style="background:#1f3a8a"></div><div class="meta"><span>5/6</span><span>$3.00</span></div></div>
  <div class="slot" style="left:997px;top:258px"><span class="no">4</span><div class="item" style="background:#5ab0c9"></div><div class="meta"><span>5/9</span><span>$3.00</span></div></div>
</section>

<section class="reviews">
  <div class="eyebrow">Testimonials</div>
  <h2 class="section-title">Happy clients say</h2>
  <span class="arrow" style="left:200px">‹</span><span class="arrow" style="left:990px">›</span>
  <div class="quote-box">
    <span class="qmark" style="left:-16px;top:-18px">“</span>
    <span class="qmark" style="right:-16px;bottom:-34px">”</span>
    <div class="stars">★★★★★</div>
    <p>" There are many variations of passages of Lorem Ipsum available, but the suffered alteration in some form, by injected humour, or randomised words which don't look even slightly believable. If you are going to use a passage of Lorem Ipsum, be sure there isn't anything embarrassing hidden."</p>
    <div class="name">STANDARD CHUNK</div>
  </div>
  <span class="btn btn-grey">View All</span>
</section>

<section class="partners">
  <h2 class="section-title">Our partners</h2>
  <div class="partner-row">
    <div class="partner-badge"><span></span></div><div class="partner-badge"><span></span></div><div class="partner-badge"><span></span></div>
    <div class="partner-badge"><span></span></div><div class="partner-badge"><span></span></div><div class="partner-badge"><span></span></div>
  </div>
  <div class="pager"><span>‹</span><span>›</span></div>
</section>

<section class="faq">
  <h2 class="section-title">Frequently asked question</h2>
  <div class="faq-list">
    <div class="faq-item"><span class="plus">+</span><span>How can I get more information about your services?</span></div>
    <div class="faq-item open"><span class="plus">−</span><span>Do I need to pay for your vending machine services or for the use of your machines?<small>No, standard vending machines services are offered at no cost to our clients.</small></span></div>
    <div class="faq-item"><span class="plus">+</span><span>After accepting SnackHarbor services, how long does it take to get the machines?</span></div>
    <div class="faq-item"><span class="plus">+</span><span>Can I select the products in the machines?</span></div>
    <div class="faq-item"><span class="plus">+</span><span>Are your vending machines in good condition?</span></div>
  </div>
  <span class="btn btn-dark">View All</span>
</section>

<section class="cta">
  <svg class="cta-bg" width="1200" height="579" viewBox="0 0 1200 579" preserveAspectRatio="none" role="img" aria-label="Dimmed city skyline at dusk">
    <defs><linearGradient id="dusk" x1="0" y1="0" x2="0" y2="1"><stop offset="0" stop-color="#2b2b2b"/><stop offset="1" stop-color="#1f1f20"/></linearGradient></defs>
    <rect width="1200" height="579" fill="url(#dusk)"/>
    <path d="M0,80 C250,230 520,240 760,130 C940,50 1080,20 1200,60 L1200,0 L0,0 Z" fill="#e6962e"/>
    <path d="M0,60 C250,200 520,210 760,100 C940,25 1080,0 1200,30 L1200,0 L0,0 Z" fill="#fff"/>
  </svg>
  <h2>Need a vending machine?</h2>
  <p class="intro">Leave us your email and a details about your business. We will arrange for a location assessment in person to getting a machine delivered and stocked as soon as possible!</p>
  <div class="lead-form">
    <div class="field">First Name</div><div class="field">Last Name</div>
    <div class="field">Email</div><div class="field">Phone</div>
    <div class="field wide">Your Organization</div>
  </div>
  <span class="btn">Submit</span>
</section>

<footer class="site-footer">
  <div class="brand">SnackHarbor</div>
  <div class="fcol" style="left:455px">
    <h5>Contact Us</h5>
    <ul>
      <li><svg width="11" height="11" viewBox="0 0 24 24"><path d="M6 2l4 5-2 3a12 12 0 006 6l3-2 5 4-3 4C10 22 2 14 2 5z" fill="#e6962e"/></svg>+1 555 014 2298</li>
      <li style="font-size:9px"><svg width="11" height="11" viewBox="0 0 24 24"><rect x="2" y="5" width="20" height="14" rx="2" fill="#e6962e"/></svg>info@snackharbor.com</li>
      <li style="font-size:8.5px"><svg width="11" height="11" viewBox="0 0 24 24"><path d="M12 2a7 7 0 017 7c0 5-7 13-7 13S5 14 5 9a7 7 0 017-7z" fill="#e6962e"/></svg>48 Harbor Crest Way,<br>Oakland, CA 94607</li>
    </ul>
  </div>
  <div class="fcol" style="left:703px">
    <h5>Quick Links</h5>
    <div class="links"><span>Home</span><span>FAQ</span><span>About Us</span><span>Contact Us</span><span>Our Machines</span><span></span><span>Services</span><span></span><span>Products</span></div>
  </div>
  <div class="social"><span></span><span class="on"></span><span></span></div>
  <div class="copy">© 2024 <b>SnackHarbor</b>. All Right Reserved</div>
  <svg class="to-top" width="18" height="18" viewBox="0 0 24 24"><path d="M12 3l8 18-8-5-8 5z" fill="#e6962e"/></svg>
</footer>

</body>
</html>
```